Wireless retailer specializing in sale / purchase of used and refurbished devices. We are an authorized dealer for " vKarro Wireless". Logos for vKarro and our logo have been included.
Business card needs to feature both locations address. We will do a reprint once we have the phone number for the second location and remove the "coming soon" text.
Cards will also need to be personalized per employee. Will post that information as well.
Any suggestions are welcome
Business
The Signal Shed
Birchmont Plaza Shopping Center
4187 Tamsin Drive
Virginia Beach, VA 23464
757.318.6942
Coming in 2014
The Signal Shed 2
Marrow Creek Shopping Center
2641 Pelfrey Rd Suite #208
Virginia Beach, VA 23452

```html
<!DOCTYPE html>
<html lang="en">
<head>
<meta charset="utf-8">
<title>The Signal Shed – Business Cards</title>
<link href="https://fonts.googleapis.com/css2?family=Saira:wght@400;500;800&display=swap" rel="stylesheet">
<style>
  :root {
    --backdrop: #eceeef;
    --card-light: #e4e5e6;
    --card-dark: #121314;
    --pattern-dark: #262829;
    --brand-blue: #1f5fb3;
    --ink: #1b1b1b;
    --rule: #3a3a3a;
    --white: #ffffff;
  }
  * { margin: 0; padding: 0; box-sizing: border-box; }
  html, body {
    width: 1200px; height: 900px; overflow: hidden;
    background: var(--backdrop);
    font-family: "Saira", "Helvetica Neue", Arial, sans-serif;
  }
  .canvas { position: relative; width: 1200px; height: 900px; }

  .card {
    position: absolute;
    width: 600px; height: 343px;
    border-radius: 4px;
    box-shadow: 0 6px 18px rgba(0,0,0,0.12);
    overflow: hidden;
  }

  /* Contact side */
  .card--contact { left: 540px; top: 70px; background: var(--card-light); }
  .wordmark {
    position: absolute; display: flex; align-items: center; gap: 12px;
    font-weight: 800; text-transform: uppercase; letter-spacing: 0.5px;
    line-height: 1;
  }
  .card--contact .wordmark { left: 40px; top: 40px; font-size: 40px; color: var(--brand-blue); }
  .wordmark__square { width: 26px; height: 26px; background: var(--brand-blue); flex: none; }

  .location { position: absolute; color: var(--ink); font-size: 15px; line-height: 22px; }
  .location--main { left: 40px; top: 150px; }
  .location--second { left: 335px; top: 205px; }
  .location__name { color: var(--brand-blue); text-transform: uppercase; font-weight: 500; font-size: 15px; }
  .location__phone { color: var(--brand-blue); font-size: 24px; letter-spacing: 1.5px; margin-top: 8px; }

  .divider { position: absolute; left: 312px; top: 200px; width: 1px; height: 100px; background: var(--rule); }

  .partner-badge {
    position: absolute; right: 40px; top: 150px;
    width: 92px; height: 42px; border-radius: 6px;
    background: var(--white); border: 1px solid #c9cacb;
  }

  /* Brand side */
  .card--brand { left: 60px; top: 487px; background: var(--card-dark); }
  .brand-pattern {
    position: absolute; inset: 0;
    background: linear-gradient(135deg, var(--pattern-dark) 0%, #1b1c1d 50%, var(--pattern-dark) 100%);
  }
  .card--brand .wordmark {
    left: 50%; top: 50%; transform: translate(-50%, -50%);
    font-size: 40px; color: var(--white); white-space: nowrap;
  }
</style>
</head>
<body>
<main class="canvas">

  <section class="card card--contact" aria-label="Business card, contact side">
    <div class="wordmark"><span class="wordmark__square"></span><span>The Signal Shed</span></div>

    <address class="location location--main">
      <div class="location__name">The Signal Shed</div>
      Birchmont Plaza Shopping Center<br>
      4187 Tamsin Drive<br>
      Virginia Beach, VA 23464
      <div class="location__phone">757.318.6942</div>
    </address>

    <div class="divider"></div>

    <div class="partner-badge" role="img" aria-label="vKarro Wireless authorized retailer badge"></div>

    <address class="location location--second">
      <div class="location__name">The Signal Shed #2</div>
      Marrow Creek Shopping Center<br>
      2641 Pelfrey Rd Suite #208<br>
      Virginia Beach, VA 23452
      <div class="location__phone">757.604.2719</div>
    </address>
  </section>

  <section class="card card--brand" aria-label="Business card, brand side">
    <div class="brand-pattern" role="img" aria-label="Repeating dark-grey brand name pattern"></div>
    <div class="wordmark"><span class="wordmark__square"></span><span>The Signal Shed</span></div>
  </section>

</main>
</body>
</html>
```